Granite Ridge Response Business Card

Side 1: Granite Ridge Response Logo (logo without Maltese cross) with industrial rope rescue related theme. Our company services - TRAINING - Fire Training, Confined Space Rescue Training, Rope Rescue training, Hazmat Training, Incident Command, EMS, Pump Operations Training. Website - graniteridgeresponse.example.
Side 2: Granite Ridge Response Fire Department Logo (logo with Maltese cross) with Firefighter related theme. Company (division) services - FIELD SERVICES - Fire Department, Stand-by Rescue, Safety, EMS, Planning. "Supporting the Emergency Response Community Since 1967"

Add contact information wherever it makes since (Name, Email, Phone).
I would like it to represent the Granite Ridge Response Fire Department Logo as a division not as a separate entity without saying it, possibly by depicting it in the background of Side 2 instead of being a standalone picture like the logo on Side 1.

```html
<!DOCTYPE html>
<html lang="en">
<head>
<meta charset="utf-8">
<title>Granite Ridge Response – Business Cards</title>
<link rel="stylesheet" href="https://fonts.googleapis.com/css2?family=Montserrat:wght@500;600;700;800&family=Lato:wght@400;700&display=swap">
<style>
  :root {
    --stage: #1c1c1e;
    --card-grey: #3a3b3e;
    --grey-deep: #2d2e31;
    --fire-red: #e8322a;
    --fire-orange: #f0552e;
    --ember: #c92a22;
    --white: #ffffff;
    --font-head: "Montserrat", sans-serif;
    --font-body: "Lato", sans-serif;
  }
  * { margin: 0; padding: 0; box-sizing: border-box; }
  html, body { width: 1200px; height: 817px; overflow: hidden; background: var(--stage); }
  .stage { position: relative; width: 1200px; height: 817px; }

  .card {
    position: absolute; width: 540px; height: 309px;
    border-radius: 18px; overflow: hidden;
    background: var(--card-grey);
    box-shadow: 0 18px 40px rgba(0,0,0,.55);
    color: var(--white);
  }
  .card--division { left: 50px; top: 70px; }
  .card--training { left: 610px; top: 438px; }

  /* ---- Division card ---- */
  .division-photo {
    position: absolute; inset: 0;
    clip-path: polygon(0 0, 100% 0, 100% 55%, 0 66%);
    background: linear-gradient(120deg, var(--fire-orange) 0%, var(--fire-red) 45%, #b9271f 100%);
  }
  .division-photo::after {
    content: ""; position: absolute; inset: 0;
    background: radial-gradient(ellipse at 62% 40%, rgba(120,20,10,.35), transparent 60%);
  }
  .divider { position: absolute; inset: 0; pointer-events: none; }

  .brand { position: absolute; display: flex; align-items: center; gap: 10px; }
  .brand__mark { width: 34px; height: 34px; border-radius: 50%; border: 2.5px solid currentColor; flex: none; }
  .brand__name { font-family: var(--font-head); font-weight: 700; letter-spacing: 1.5px; line-height: 1.1; }

  .division-brand { left: 30px; top: 108px; color: var(--white); }
  .division-brand .brand__name { font-size: 18px; }

  .contact { position: absolute; right: 28px; top: 30px; text-align: right; }
  .contact__name { font-family: var(--font-head); font-weight: 800; font-size: 19px; letter-spacing: .5px; }
  .contact__title { font-family: var(--font-body); font-size: 13px; margin-top: 2px; }
  .contact__line { display: flex; justify-content: flex-end; align-items: center; gap: 8px; font-family: var(--font-body); font-size: 12px; margin-top: 8px; }
  .contact__icon { width: 18px; height: 18px; background: var(--white); border-radius: 3px; display: grid; place-items: center; }

  .pill {
    position: absolute; border-radius: 14px;
    background: var(--fire-red); border: 1.5px solid var(--white);
    font-family: var(--font-body); font-weight: 700; color: var(--white);
    white-space: nowrap;
  }
  .tagline-pill { left: 34px; top: 180px; padding: 4px 14px; font-size: 11.5px; transform: rotate(-3.6deg); transform-origin: left center; }

  .services { position: absolute; list-style: none; font-family: var(--font-head); font-weight: 500; font-size: 11.5px; letter-spacing: .3px; }
  .services li { display: flex; align-items: center; gap: 7px; margin-bottom: 5px; }
  .services li::before { content: ""; width: 5px; height: 5px; border-radius: 50%; background: var(--fire-red); flex: none; }
  .services--col1 { left: 40px; top: 236px; }
  .services--col2 { left: 215px; top: 228px; }
  .services--col3 { left: 395px; top: 220px; }

  /* ---- Training card ---- */
  .training-photo {
    position: absolute; inset: 0;
    background: linear-gradient(135deg, #3f4044 0%, #333437 50%, #2b2c2f 100%);
  }
  .training-photo::after {
    content: ""; position: absolute; inset: 0;
    background: radial-gradient(ellipse at 45% 30%, rgba(255,255,255,.06), transparent 60%);
  }
  .training-red {
    position: absolute; inset: 0;
    clip-path: polygon(0 60%, 100% 38%, 100% 100%, 0 100%);
    background: linear-gradient(135deg, var(--fire-red) 0%, var(--fire-orange) 55%, var(--ember) 100%);
  }
  .training-brand { left: 160px; top: 52px; color: var(--fire-red); }
  .training-brand .brand__name { font-size: 20px; }
  .web-pill { left: 150px; top: 142px; padding: 4px 14px; font-size: 12px; letter-spacing: 2px; transform: rotate(-7.2deg); transform-origin: left center; }

  .training-list { position: absolute; list-style: none; font-family: var(--font-body); font-size: 13px; color: var(--white); }
  .training-list li { display: flex; align-items: center; gap: 6px; margin-bottom: 3px; }
  .training-list li::before { content: ""; width: 4px; height: 4px; border-radius: 50%; background: var(--white); flex: none; }
  .training-list--main { left: 36px; top: 200px; }
  .training-list--main li:first-child { font-family: var(--font-head); font-weight: 600; letter-spacing: .5px; }
  .training-list--extra { left: 330px; top: 162px; }
</style>
</head>
<body>
<main class="stage">

  <!-- Side 2: Fire Department division -->
  <section class="card card--division">
    <div class="division-photo" role="img" aria-label="Firefighters in turnout gear walking through smoke, tinted red"></div>
    <svg class="divider" width="540" height="309" viewBox="0 0 540 309">
      <line x1="0" y1="204" x2="540" y2="170" stroke="#ffffff" stroke-width="1.5"/>
    </svg>

    <div class="brand division-brand">
      <span class="brand__mark"></span>
      <span class="brand__name">GRANITE RIDGE<br>RESPONSE</span>
    </div>

    <div class="contact">
      <p class="contact__name">DANIEL R. WHITMORE</p>
      <p class="contact__title">Managing Director</p>
      <p class="contact__line">+00 555 201 44
        <span class="contact__icon">
          <svg width="12" height="12" viewBox="0 0 24 24"><path fill="#e8322a" d="M6.6 10.8a15.5 15.5 0 0 0 6.6 6.6l2.2-2.2c.3-.3.7-.4 1-.2 1.1.4 2.3.6 3.6.6.6 0 1 .4 1 1V20c0 .6-.4 1-1 1A17 17 0 0 1 3 4c0-.6.4-1 1-1h3.5c.6 0 1 .4 1 1 0 1.3.2 2.5.6 3.6.1.3 0 .7-.2 1z"/></svg>
        </span>
      </p>
      <p class="contact__line">office@graniteridgeresponse.example
        <span class="contact__icon">
          <svg width="12" height="12" viewBox="0 0 24 24"><rect x="2" y="5" width="20" height="14" rx="1" fill="none" stroke="#e8322a" stroke-width="2"/><path d="M2 6l10 7 10-7" fill="none" stroke="#e8322a" stroke-width="2"/></svg>
        </span>
      </p>
    </div>

    <p class="pill tagline-pill">Supporting the Emergency Response Community Since 1967</p>

    <ul class="services services--col1"><li>FIELD SERVICES</li><li>FIRE DEPARTMENT</li></ul>
    <ul class="services services--col2"><li>STAND-BY RESCUE</li><li>SAFETY</li></ul>
    <ul class="services services--col3"><li>EMS</li><li>PLANNING</li></ul>
  </section>

  <!-- Side 1: Training -->
  <section class="card card--training">
    <div class="training-photo" role="img" aria-label="Faded photo of an industrial rope rescue with harness and ropes"></div>
    <div class="training-red"></div>
    <svg class="divider" width="540" height="309" viewBox="0 0 540 309">
      <line x1="0" y1="185" x2="540" y2="117" stroke="#ffffff" stroke-width="1.5"/>
    </svg>

    <div class="brand training-brand">
      <span class="brand__mark"></span>
      <span class="brand__name">GRANITE RIDGE<br>RESPONSE</span>
    </div>

    <p class="pill web-pill">graniteridgeresponse.example</p>

    <ul class="training-list training-list--main">
      <li>TRAINING</li>
      <li>Fire Training</li>
      <li>Confined Space Rescue Training</li>
      <li>Rope Rescue training</li>
    </ul>
    <ul class="training-list training-list--extra">
      <li>Hazmat Training</li>
      <li>Incident Command</li>
      <li>EMS</li>
      <li>Pump Operations Training</li>
    </ul>
  </section>

</main>
</body>
</html>
```